NAT stands for Nell and Tova - teenager girls that will provide makeup and photography services for proms, weddings, graduations and other special events. The design should be bright and cheery and have the teenage audience it will be directed to in mind. I want the word "NAT" to be a part of the postcard and be essentially a logo by itself with the names somewhere under it.

Target Market(s)

Teenagers

Industry/Entity Type

Makeup

Requirements
Must have
• The Word "NAT" as the logo for the make up and photography services with the girls name in smaller font somewhere to identify what "NAT" stands for.
Nice to have
• I like circles and bright colors. I like tie dye too. There should be room to put a couple photos of their work on the postcard.
Should not have
• No address will be proved

```html
<!DOCTYPE html>
<html lang="en">
<head>
<meta charset="utf-8">
<title>NAT Makeup &amp; Photography Postcard</title>
<link rel="stylesheet" href="https://fonts.googleapis.com/css2?family=Questrial&display=swap">
<style>
  :root {
    --paper: #ffffff;
    --ink: #111111;
    --navy: #2e3192;
    --magenta: #b0228c;
    --sun: #f2e21b;
    --panel: #e6b9dd;
    --rule: #1a1a1a;
  }
  * { margin: 0; padding: 0; box-sizing: border-box; }
  html, body {
    width: 1200px; height: 928px; overflow: hidden; background: var(--paper);
  }
  .postcard {
    position: relative; width: 1200px; height: 928px; overflow: hidden;
    background: var(--paper); color: var(--ink);
    font-family: "Questrial", sans-serif;
  }
  .dot-field { position: absolute; left: 0; top: 0; }

  .brand {
    position: absolute; left: 858px; top: 95px; width: 300px;
    text-align: center;
  }
  .brand-name {
    display: inline-flex; align-items: center; gap: 16px;
    font-size: 96px; line-height: 1; letter-spacing: 5px; color: var(--ink);
  }
  .brand-mark {
    width: 28px; height: 28px; border-radius: 50%; background: var(--magenta);
    flex: none;
  }
  .brand-names {
    margin-top: 62px; font-size: 20px; letter-spacing: 2px; color: var(--ink);
  }

  .services {
    position: absolute; left: 845px; top: 331px; width: 333px; height: 474px;
    background: var(--panel); border-radius: 33px; text-align: center;
    padding-top: 14px;
  }
  .services-title { font-size: 36px; line-height: 45px; font-weight: 400; }
  .services-rule {
    width: 290px; height: 2px; background: var(--rule); margin: 10px auto 12px;
  }
  .services-list { list-style: none; font-size: 31px; line-height: 36px; }
  .services-rule.lower { margin: 10px auto 6px; }
  .cta {
    font-weight: 400; font-size: 38px; line-height: 51px;
    -webkit-text-stroke: 1px var(--ink);
  }

  .contact {
    position: absolute; right: 27px; top: 816px; text-align: right;
    font-size: 29px; line-height: 45px; font-style: normal;
  }
  .contact-phone { padding-right: 6px; }
</style>
</head>
<body>
<main class="postcard">
  <svg class="dot-field" width="640" height="928" viewBox="0 0 640 928" role="img"
       aria-label="Decorative scattered polka dots in navy, magenta, yellow and black">
    <defs>
      <linearGradient id="dot-tones" x1="0" y1="0" x2="0.4" y2="1">
        <stop offset="0" stop-color="#2e3192"/>
        <stop offset="0.5" stop-color="#b0228c"/>
        <stop offset="1" stop-color="#f2e21b"/>
      </linearGradient>
    </defs>
    <path d="M0 0 H500 C300 60 190 200 190 430 C190 640 340 770 620 928 H0 Z"
          fill="url(#dot-tones)" opacity="0.8"/>
  </svg>

  <header class="brand">
    <div class="brand-name"><span class="brand-mark"></span>NAT</div>
    <p class="brand-names">Nell and Tova</p>
  </header>

  <section class="services">
    <h1 class="services-title">Makeup<br>&amp; Photography</h1>
    <div class="services-rule"></div>
    <ul class="services-list">
      <li>Prom</li>
      <li>Weddings</li>
      <li>Graduations</li>
      <li>Special Dates</li>
      <li>Dances</li>
      <li>Special Occasions</li>
    </ul>
    <div class="services-rule lower"></div>
    <p class="cta">Call or<br>E-mail Today</p>
  </section>

  <address class="contact">
    <div class="contact-phone">612-555-0147</div>
    <div class="contact-email">NATmakeupandphoto@example.com</div>
  </address>
</main>
</body>
</html>
```